Upsell Vertical Banner Ad Design For B2B Marketing Agency Vertical 768px × 1180px IS THE SIZE

I need a banner made for my website www.brightlanepromotionhub.biz This banner will be an upsell advertisement for after someone signs up for my monthly program. When they login to their account for the 1st time I will give them the chance to upgrade their account to our annual program with just one click.

this is a page that upsells it currently to give you an idea how we market ourselves:
https://tlpx.pagevault-example.com/page/tlp-annual-upsell

Use this content:

Are You Ready To Commit To Taking Your Business To The Next Level?

Because We're In This For The Long-Haul and Dedicated To Your Success...

Save $300 By Upgrading To An Annual Membership And Pay Only $74/mth

((BUTTON))Yes, Upgrade My Plan Right Now!

*Must prepay the full year at only $898/yr!

Target Market(s)

business owners

Industry/Entity Type

Marketing

Requirements
Must have
• 768px × 1180px IS THE SIZE vertical

Use this content:

Nice to have
• Use this content:

Should not have
• Use this content:

```html
<!DOCTYPE html>
<html lang="en">
<head>
<meta charset="utf-8">
<title>Annual Membership Upgrade Banner</title>
<link rel="stylesheet" href="https://fonts.googleapis.com/css2?family=Krona+One&family=Oswald:wght@600;700&family=Montserrat:wght@500&display=swap">
<style>
  :root {
    --stage: #5c5c5c;
    --red: #cc0000;
    --blue-deep: #0561ab;
    --blue-bright: #0a7ad6;
    --white: #ffffff;
    --ink-blue: #165c9e;
    --ink-dark: #2b2b2b;
    --green-dark: #2a7f32;
    --green-light: #4caf50;
    --note-bg: #ececec;
    --note-line: #d8d8d8;
    --note-ink: #444444;
  }
  * { box-sizing: border-box; margin: 0; padding: 0; }
  html, body { width: 1200px; height: 1200px; overflow: hidden; }
  body { background: var(--stage); position: relative; }

  .banner {
    position: absolute; left: 275px; top: 100px;
    width: 650px; height: 1000px;
    background: var(--white); overflow: hidden;
  }
  .headline-band {
    position: absolute; left: 0; top: 0; width: 650px; height: 284px;
    background: var(--red);
  }
  .headline-lead {
    position: absolute; left: 0; top: 64px; width: 650px; text-align: center;
    font-family: "Krona One", sans-serif; font-size: 45px; line-height: 1;
    letter-spacing: -2px; color: var(--white);
  }
  .headline-pill {
    position: absolute; left: 47px; top: 122px; width: 556px; height: 58px;
    background: var(--white); border-radius: 10px;
    display: flex; align-items: center; justify-content: center;
    font-family: "Oswald", sans-serif; font-weight: 600; font-size: 35px;
    color: var(--ink-blue); letter-spacing: 0.2px;
  }
  .headline-close {
    position: absolute; left: 0; top: 184px; width: 650px; text-align: center;
    font-family: "Oswald", sans-serif; font-weight: 700; font-size: 62px;
    line-height: 1.2; color: var(--white);
  }

  .promise-band { position: absolute; left: 0; top: 284px; width: 650px; height: 540px; }
  .promise-band svg { display: block; }
  .promise {
    position: absolute; left: 0; top: 305px; width: 650px; text-align: center;
    font-family: "Krona One", sans-serif; color: var(--white); line-height: 1;
  }
  .promise-because { font-size: 36px; letter-spacing: 34px; margin-left: 34px; }
  .promise-line { font-size: 27px; letter-spacing: -1.5px; margin-top: 11px; }
  .promise-line:first-of-type { margin-top: 14px; }
  .promise-close { font-size: 40px; letter-spacing: -2px; margin-top: 10px; }

  .offer {
    position: absolute; left: 47px; top: 530px; width: 556px; height: 218px;
    border-radius: 7px; overflow: hidden;
    box-shadow: 0 12px 16px rgba(0, 40, 90, 0.35);
  }
  .offer-price {
    height: 126px; background: var(--red);
    display: flex; align-items: center; justify-content: center;
    font-family: "Oswald", sans-serif; font-weight: 700; font-size: 104px;
    color: var(--white); line-height: 1;
  }
  .offer-terms {
    height: 92px; background: linear-gradient(90deg, #ececec, #ffffff);
    display: flex; flex-direction: column; align-items: center; justify-content: center;
    font-family: "Krona One", sans-serif; font-size: 17px; letter-spacing: -0.8px;
    color: var(--ink-dark); line-height: 1.8;
  }

  .upgrade-button { position: absolute; left: 82px; top: 774px; width: 510px; height: 130px; }
  .upgrade-button svg { position: absolute; left: 0; top: 0; }
  .upgrade-label {
    position: absolute; left: 0; top: 10px; width: 510px; text-align: center;
    font-family: "Oswald", sans-serif; font-weight: 700; font-size: 42px;
    line-height: 48px; color: var(--white);
  }

  .fine-print {
    position: absolute; left: 51px; top: 931px; width: 548px; height: 44px;
    background: var(--note-bg); border: 1px solid var(--note-line); border-radius: 3px;
    display: flex; align-items: center; justify-content: center;
    font-family: "Montserrat", sans-serif; font-weight: 500; font-size: 15px;
    letter-spacing: 2px; color: var(--note-ink);
  }
</style>
</head>
<body>
  <main class="banner">
    <header class="headline-band">
      <h1 class="headline-lead">ARE YOU READY</h1>
      <p class="headline-pill">TO COMMIT TO TAKING YOUR BUSINESS</p>
      <p class="headline-close">TO THE NEXT LEVEL?</p>
    </header>

    <div class="promise-band">
      <svg width="650" height="540" viewBox="0 0 650 540" aria-hidden="true">
        <defs>
          <linearGradient id="promiseFill" x1="0" y1="0" x2="1" y2="0.3">
            <stop offset="0" stop-color="var(--blue-deep)"/>
            <stop offset="1" stop-color="var(--blue-bright)"/>
          </linearGradient>
        </defs>
        <path d="M0 0 H650 V518 Q650 528 640 530 L325 538 L10 530 Q0 528 0 518 Z" fill="url(#promiseFill)"/>
      </svg>
    </div>

    <section class="promise">
      <p class="promise-because">BECAUSE</p>
      <p class="promise-line">WE'RE IN THIS</p>
      <p class="promise-line">FOR THE LONG-HAUL</p>
      <p class="promise-line">AND DEDICATED</p>
      <p class="promise-close">TO YOUR SUCCESS...</p>
    </section>

    <section class="offer">
      <p class="offer-price">SAVE $300</p>
      <div class="offer-terms">
        <p>By Upgrading To An Annual Membership</p>
        <p>And Pay Only $74/mth</p>
      </div>
    </section>

    <a class="upgrade-button" href="#upgrade">
      <svg width="510" height="130" viewBox="0 0 510 130" aria-hidden="true">
        <defs>
          <linearGradient id="buttonFill" x1="0" y1="0" x2="1" y2="0">
            <stop offset="0" stop-color="var(--green-dark)"/>
            <stop offset="1" stop-color="var(--green-light)"/>
          </linearGradient>
        </defs>
        <path d="M4 0 H506 Q510 0 510 4 L499 110 L267 128 L14 112 L0 4 Q0 0 4 0 Z" fill="url(#buttonFill)"/>
        <path d="M14 112 L267 128 L499 110 L498 116 L267 130 L15 118 Z" fill="#2c8a34"/>
      </svg>
      <span class="upgrade-label">YES, UPGRADE MY PLAN<br>RIGHT NOW!</span>
    </a>

    <p class="fine-print">*Must prepay the full year at only $898/yr!</p>
  </main>
</body>
</html>
```